Flyer To Solicit Donations for a Good Cause

Hi. I am running the distance of a marathon race to solicit donations for a charitable cause. I need a well designed flyer to help me solicit support from friends and others. The copy for the flyer is attached. There is a significant amount of written text so it will need to be laid out in a way that is easy to read but also mixes well with some good images and design appeal. I am open to creative ideas. I have also attached my photo and a photo of me shaking hands with Mayor Derlin of Delphi and president of the Brastow Harmonic Fellowship. Also there are some photos of the areas. These photos don't have to be used except for the one of me shaking hands with the Mayor and a caption underneath it. Otherwise, I am open to other stock photos or graphics. Feel free to contact me if you have questions. Thank you !

Update: ONE SIDED FLYER

• Photo of the Mayor and Toby with the caption identifying us; All of the copy/text.

```html
<!DOCTYPE html>
<html lang="en">
<head>
<meta charset="utf-8">
<title>A Special Journey – Toby Marlowe</title>
<link href="https://fonts.googleapis.com/css2?family=Roboto+Condensed:ital,wght@0,400;0,700;1,400;1,700&family=PT+Sans:ital,wght@0,400;0,700;1,400&display=swap" rel="stylesheet">
<style>
:root{
  --blue:#1f67b1;
  --blue-deep:#1a5a9e;
  --orange:#e98a25;
  --panel:rgba(30,30,30,.72);
  --ink:#2a2a2a;
  --white:#ffffff;
}
*{box-sizing:border-box;margin:0;padding:0}
html,body{width:848px;height:1200px;overflow:hidden;background:#fff}
.flyer{position:relative;width:848px;height:1200px;overflow:hidden;font-family:"Roboto Condensed",sans-serif;color:var(--white)}

/* hero */
.hero{position:absolute;left:0;top:0;width:848px;height:492px}
.hero-runners{position:absolute;left:0;top:0;width:424px;height:492px;background:linear-gradient(160deg,#3f86cc 0%,#2a6fb5 45%,#5a8fbf 100%)}
.hero-ruins{position:absolute;left:424px;top:0;width:424px;height:492px;background:linear-gradient(180deg,#f2f2f2 0%,#bdbdbd 45%,#6f6f6f 75%,#3e3e3e 100%)}
.hero-portrait{position:absolute;left:262px;top:30px;width:294px;height:462px;border-radius:120px 120px 0 0;background:linear-gradient(180deg,#3a3f4a 0%,#2b3340 40%,#1f2530 100%)}
.hero-title{position:absolute;left:33px;top:86px;z-index:2}
.hero-title h1{font-weight:700;font-size:36px;line-height:40px}
.hero-title .sub{font-size:29px;line-height:38px;font-weight:400}
.hero-title .name{font-weight:700;font-size:36px;margin-top:18px;line-height:42px}
.hero-title .date{font-weight:700;font-size:23px;margin-top:6px}
.contact{position:absolute;left:482px;top:42px;display:flex;align-items:center;gap:18px;font-weight:700;font-size:20px}

/* story */
.story{position:absolute;left:0;top:492px;width:848px;height:426px;background:linear-gradient(180deg,#6f7c86 0%,#8a8f7d 35%,#6e7a4c 70%,#57663a 100%)}
.heading-bar{position:absolute;left:28px;width:396px;background:var(--orange);font-weight:700;font-size:16.5px;line-height:21px;padding:4px 8px}
.heading-first{top:16px;height:50px}
.heading-second{top:234px;height:30px}
.text-panel{position:absolute;left:28px;width:396px;background:var(--panel);font-family:"PT Sans",sans-serif;font-size:12px;line-height:15.5px;padding:6px 8px}
.text-panel p{margin-bottom:8px}
.text-panel .web{font-family:"Roboto Condensed",sans-serif;font-weight:700;font-size:16px;margin-bottom:0}
.panel-first{top:66px;height:162px}
.panel-second{top:264px;height:154px}
.meeting-photo{position:absolute;left:470px;top:28px;width:365px;height:340px;border-radius:50%;border:5px solid #fff;background:linear-gradient(160deg,#d9e2ea 0%,#a7b7c6 45%,#5c4a3e 100%)}
.caption{position:absolute;left:435px;top:370px;width:400px;background:var(--orange);font-weight:700;font-size:13px;line-height:17px;text-align:center;padding:4px 10px}

/* steps */
.steps{position:absolute;left:20px;top:930px;width:810px;color:var(--ink);font-family:"PT Sans",sans-serif;font-style:italic;font-size:12.4px;line-height:15px;list-style:none}
.steps li{display:flex;margin-bottom:9px}
.steps .num{width:22px;flex:none}

/* footer */
.footer{position:absolute;left:0;top:1108px;width:848px;height:92px;background:var(--blue-deep);display:flex;align-items:center;justify-content:center;font-style:italic;font-size:28px}
</style>
</head>
<body>
<div class="flyer">
  <header class="hero">
    <div class="hero-runners" role="img" aria-label="Blue-toned photo of runners' legs on a road"></div>
    <div class="hero-ruins" role="img" aria-label="Black and white photo of the ancient round temple ruins at Delphi"></div>
    <div class="hero-portrait" role="img" aria-label="Portrait of Toby Marlowe in a dark blazer"></div>
    <div class="hero-title">
      <h1>A Special Journey</h1>
      <p class="sub">For Your Specific Prayers<br>&amp; For An Important<br>Ancient Cause<br>By</p>
      <p class="name">Toby Marlowe</p>
      <p class="date">April 2016</p>
    </div>
    <div class="contact">
      <svg width="36" height="24" viewBox="0 0 36 24" aria-hidden="true"><rect x="1" y="1" width="34" height="22" fill="none" stroke="#fff" stroke-width="2"/><path d="M1 1 L18 14 L35 1" fill="none" stroke="#fff" stroke-width="2"/></svg>
      <span>tmarlowe@marlowefenn.com</span>
    </div>
  </header>

  <section class="story" role="group" aria-label="About the journey">
    <h2 class="heading-bar heading-first">This coming April 2016 Toby Marlowe will make a special running journey of 26 miles</h2>
    <div class="text-panel panel-first">
      <p>through the ancient lands of Apollo and Athena at Delphi on Mt. Parnassus in Greece.</p>
      <p>Toby will adorn his running outfit with special cloth strips that will contain written prayers and petitions of people who will sponsor his journey by making a charitable donation to the Brastow Harmonic Fellowship, an organization that preserves the land and the Delphic culture.</p>
      <p class="web">www.brastow-harmonic-fellowship.org</p>
    </div>
    <h2 class="heading-bar heading-second">The concept is simple and very powerful</h2>
    <div class="text-panel panel-second">
      <p>as Toby runs, your written prayer on a cloth strip will flow and emanate in the wind --- being blessed by the spirits of this ancient and magical land --- asking unto the wind that your prayer be answered. This type of prayer practice dates back to ancient times. The Tibetan culture commonly uses prayer flags with special mantras and symbols.</p>
      <p>Will you make a prayer for yourself or a loved and support a good cause? Here is how to get your prayer started:</p>
    </div>
    <div class="meeting-photo" role="img" aria-label="Photo of Toby shaking hands with Mayor Derlin"></div>
    <p class="caption">Toby with Mayor Derlin of Delphi and president of the Brastow Harmonic Fellowship</p>
  </section>

  <ol class="steps">
    <li><span class="num">1)</span><span>Decide what you want your prayer, petition or intention to be.</span></li>
    <li><span class="num">2)</span><span>Define your prayer, petition or intention by writing it down.</span></li>
    <li><span class="num">3)</span><span>Refine it is concise, clear&amp; specific. (18 words or less is ideal for each strip cloth).</span></li>
    <li><span class="num">4)</span><span>Contact Toby at tmarlowe@marlowefenn.com and tell him how many prayer cloth strips you wish to obtain. Toby will then send you the cloth for you to write your prayer and send back to him or he will write out the prayer for you. Toby can also answer any questions you may have.</span></li>
    <li><span class="num">5)</span><span>A minimum donation of $50 for each prayer cloth is requested. Checks can be made to the “Marlowe Fenn Trust Account/Brastow Harmonic Fellowship” and mail to Toby T. Marlowe, Marlowe Fenn PLC, 1480 Alder Court, Ste. 204 Lakeview, Ohio 43210 or though online payment instructions sent by email from Toby as requested.</span></li>
  </ol>

  <footer class="footer">Your Prayer Can Make A Difference For You &amp; For A Good Cause !</footer>
</div>
</body>
</html>
```